Menu Needed for Chicken Wing Concept

We are looking for a print menu for a local wing restaurant called Pollo Barn. This restaurant serves chicken wings and tenders, soft drinks, boozy drinks, dips and fries. The company colors are red and black with slate grey and should be incorporated into the design. I have included renders to show you what the restaurant looks like, source files for the logo (we prefer the "Pollo Barn" logo over the "Pollo Barn Chicken Wings" logo), and a menu in text format. Please let me know if you need any further direction. We prefer trifold menu, standard paper size 8.5 x 11". The client has just given us an example of what they like. You can see the images here:
https://www.filebinly.net/sh/tkrmepdaw/XBQPLofrTyUvMnEsKaZdCwJhG?dl=0 Thanks!

Target Market(s)

Americans of all ages and ethnicities

Industry/Entity Type

Restaurant

Requirements
Must have
• Logo colors, all info included

```html
<!DOCTYPE html>
<html lang="en">
<head>
<meta charset="utf-8">
<title>Pollo Barn Menu</title>
<link rel="stylesheet" href="https://fonts.googleapis.com/css2?family=Crimson+Pro:wght@400;700&family=Montserrat:wght@700;800&family=Roboto+Condensed:wght@400;700&display=swap">
<style>
:root{
  --slate:#625d5d;
  --black:#0b0b0b;
  --red:#d9261c;
  --white:#ffffff;
  --band:#5f5a5a;
}
*{box-sizing:border-box;margin:0;padding:0}
html,body{width:1200px;height:856px;overflow:hidden;background:var(--slate)}
.canvas{position:relative;width:1200px;height:856px;background:var(--slate)}
.board{position:absolute;left:18px;top:18px;width:1164px;height:820px;background:var(--black)}
.abs{position:absolute;white-space:nowrap}
.cond{font-family:"Roboto Condensed",sans-serif;font-weight:700;color:var(--white)}
.wide{font-family:"Montserrat",sans-serif;font-weight:800;color:var(--white)}
.serif{font-family:"Crimson Pro",serif;color:var(--white)}
.red{color:var(--red)}

.brand-name{left:79px;top:60px;font-family:"Roboto Condensed",sans-serif;font-weight:700;font-size:58px;letter-spacing:2px;color:var(--red);line-height:1}
.menu-mark{left:169px;top:150px;width:134px;height:95px;background:linear-gradient(#3e3b3b,#2c2a2a);border-radius:4px}

.section-label{font-family:"Crimson Pro",serif;font-size:14px;color:var(--red);text-transform:uppercase}
.flavor-line{font-family:"Crimson Pro",serif;font-size:13.2px;color:var(--white)}

.frame{position:absolute;border:5px solid var(--red)}
.ribbon{position:absolute}
.ribbon svg{position:absolute;inset:0;width:100%;height:100%}
.ribbon span{position:relative;display:flex;align-items:center;justify-content:center;height:100%;font-family:"Crimson Pro",serif;font-weight:700;color:var(--white);white-space:nowrap}

.band{position:absolute;background:var(--band);color:var(--white);text-align:center;font-family:"Montserrat",sans-serif;font-weight:700}

.price-box{position:absolute;border:2px solid var(--white);color:var(--red);font-family:"Montserrat",sans-serif;font-weight:800;font-size:12px;display:flex;align-items:center;justify-content:center}

.grid-row{font-size:12px}
.side-item{font-size:12px;line-height:12px;letter-spacing:1.4px}
.divider{position:absolute;width:1px;background:var(--white);top:611px;height:66px}
.combo-dash{position:absolute;left:59px;top:503px;width:341px;height:290px;border:2px dashed var(--white)}
</style>
</head>
<body>
<div class="canvas">
  <div class="board"></div>

  <div class="abs brand-name">POLLO BARN</div>
  <div class="abs menu-mark" role="img" aria-label="Decorative MENU lettering with flourishes"></div>

  <div class="abs section-label" style="left:52px;top:292px">Wang Flavors</div>
  <div class="abs flavor-line" style="left:52px;top:308px">The Reaper • Traditional Hot • New Orleans Spicy</div>
  <div class="abs flavor-line" style="left:52px;top:325px">Spicy Korean BBQ • Spicy Garlic • Bangin Jamaican Jerk</div>
  <div class="abs flavor-line" style="left:52px;top:341px">Mango Haberero • Pineapple Bang • Gojugang • Mild • Texas BBQ</div>
  <div class="abs flavor-line" style="left:52px;top:357px">Teriyaki • Garlic Parmesan • Lemon Pepper • Honey BBQ</div>
  <div class="abs section-label" style="left:52px;top:394px">Dry Rubs</div>
  <div class="abs flavor-line" style="left:52px;top:411px">LEMON PEPPER • NEW ORLEANS SPICY • GARLIC PARMESEAN</div>

  <!-- By the piece -->
  <div class="frame" style="left:447px;top:63px;width:457px;height:380px"></div>
  <div class="ribbon" style="left:598px;top:47px;width:156px;height:37px">
    <svg viewBox="0 0 100 30" preserveAspectRatio="none"><polygon points="0,0 100,0 94,15 100,30 0,30 6,15" fill="#d9261c"/><polygon points="4,3 96,3 91,15 96,27 4,27 9,15" fill="none" stroke="#fff" stroke-dasharray="1 2" vector-effect="non-scaling-stroke"/></svg>
    <span style="font-size:18px">BY THE PIECE</span>
  </div>
  <div class="abs wide red" style="left:464px;top:80px;font-size:15px">WANGS</div>
  <div class="abs cond" style="left:467px;top:110px;font-size:13px">Boneless</div>
  <div class="abs cond" style="left:656px;top:110px;font-size:13px">50/50</div>
  <div class="abs cond" style="left:815px;top:110px;font-size:13px">Traditional</div>

  <div class="abs cond grid-row" style="left:469px;top:134px;line-height:22.4px">10<br>15<br>20<br>30<br>50<br>100</div>
  <div class="abs cond grid-row" style="left:493px;top:134px;line-height:22.4px">$11.99 &nbsp;(2 Flvs.)<br>$17.99 &nbsp;(2 Flvs.)<br>$22.99 &nbsp;(3 Flvs)<br>$35.29 &nbsp;(4 Flvs)<br>$58.99 &nbsp;(5 Flvs)<br>$110.99 (6 Flvs)</div>
  <div class="abs cond grid-row" style="left:618px;top:134px;line-height:22.4px">10<br>15<br>20<br>30<br>50<br>100</div>
  <div class="abs cond grid-row" style="left:649px;top:134px;line-height:22.4px">$12.99 &nbsp;(2 Flvs.)<br>$19.39 &nbsp;(2 Flvs.)<br>$25.66 &nbsp;(3 Flvs.)<br>$38.29 (4 Flvs.)<br>$63.09 &nbsp;(5 Flvs.)<br>$120.99 (6 Flvs.)</div>
  <div class="abs cond grid-row" style="left:764px;top:134px;line-height:22.4px">10<br>15<br>20<br>30<br>50<br>100</div>
  <div class="abs cond grid-row" style="left:793px;top:134px;line-height:22.4px">$12.99 &nbsp;(2 Flvs.)<br>$19..39 &nbsp;(2Flvs.)<br>$25.66 (3 Flvs.)<br>$38.29 (4 Flvs.)<br>$63.09 (5 Flvs.)<br>$120.99 (6 Flvs.)</div>

  <div class="band" style="left:454px;top:268px;width:441px;height:16px;font-size:10px;line-height:16px;letter-spacing:2px">Dips Sold Separately</div>

  <div class="abs wide red" style="left:474px;top:290px;font-size:15px">TENDERS</div>
  <div class="abs cond" style="left:475px;top:313px;font-size:12.5px;line-height:20.5px">4<br>7<br>15<br>20<br>30</div>
  <div class="abs cond" style="left:502px;top:313px;font-size:12.5px;line-height:20.5px">$7.99<br>$12.69<br>$22.49<br>$30.89<br>$40.99</div>
  <div class="abs cond" style="left:559px;top:313px;font-size:12.5px;line-height:20.5px">1 flavor &amp; 1 Dip<br>2 flavors &amp; 2 Dips<br>3 flavors &amp; 3 Dips<br>4 flavors &amp; 4 Dips<br>4 flavors &amp; 5 Dips</div>
  <div class="band" style="left:454px;top:416px;width:441px;height:16px;font-size:8px;line-height:16px">All Fries, Veggies, and Dips Sold Separately.</div>

  <!-- Sides -->
  <div class="frame" style="left:922px;top:64px;width:240px;height:379px"></div>
  <div class="ribbon" style="left:951px;top:46px;width:182px;height:38px">
    <svg viewBox="0 0 100 30" preserveAspectRatio="none"><polygon points="0,0 100,0 94,15 100,30 0,30 6,15" fill="#d9261c"/><polygon points="4,3 96,3 91,15 96,27 4,27 9,15" fill="none" stroke="#fff" stroke-dasharray="1 2" vector-effect="non-scaling-stroke"/></svg>
    <span style="font-size:21px">SIDES</span>
  </div>
  <div class="abs wide" style="left:950px;top:100px;font-size:15px;letter-spacing:1px">Fries</div>
  <div class="abs wide side-item" style="left:950px;top:125px">Regular<br>Reg. $2.99 &nbsp;Lrg $4.99</div>
  <div class="abs wide side-item" style="left:950px;top:161px">Cajun fries<br>Reg. $2.99 &nbsp;Lrg $4.99</div>
  <div class="abs wide side-item" style="left:950px;top:195px">House fries<br>Reg. $2.99 &nbsp;Lrg $4.99</div>
  <div class="abs wide side-item" style="left:950px;top:249px;line-height:14px">Garlic Parmesan Fries<br>Reg. $3.99 &nbsp;Lrg. $5.49</div>
  <div class="abs wide side-item" style="left:950px;top:291px;line-height:14px">Cheese Fries<br>Reg. $3.99 &nbsp;Lrg. $5.49</div>
  <div class="abs wide side-item" style="left:950px;top:328px;line-height:14px">Chili Cheese fries<br>Reg. $4.99 &nbsp;Lrg $5.99</div>
  <div class="abs wide side-item" style="left:950px;top:373px;line-height:19px">Veggies<br>$1.79</div>

  <!-- Combo -->
  <div class="frame" style="left:45px;top:490px;width:369px;height:316px"></div>
  <div class="combo-dash"></div>
  <div class="ribbon" style="left:124px;top:471px;width:198px;height:39px">
    <svg viewBox="0 0 100 30" preserveAspectRatio="none"><polygon points="0,0 100,0 94,15 100,30 0,30 6,15" fill="#d9261c"/><polygon points="4,3 96,3 91,15 96,27 4,27 9,15" fill="none" stroke="#fff" stroke-dasharray="1 2" vector-effect="non-scaling-stroke"/></svg>
    <span style="font-size:31px">COMBO</span>
  </div>
  <svg class="abs" style="left:63px;top:522px" width="108" height="41" viewBox="0 0 108 41"><ellipse cx="54" cy="20.5" rx="53" ry="20" fill="#d9261c"/></svg>
  <div class="abs wide" style="left:75px;top:530px;font-size:19px;letter-spacing:.5px;color:#2a0605">Wangs</div>
  <div class="abs cond" style="left:198px;top:557px;font-size:12.5px">Boneless</div>
  <div class="abs cond" style="left:264px;top:557px;font-size:12.5px">50/50</div>
  <div class="abs cond" style="left:324px;top:557px;font-size:12.5px">Bone-in</div>
  <div class="abs cond" style="left:84px;top:584px;font-size:12.5px;line-height:18px">6 piece &nbsp;&nbsp;(1 flv'rs)<br>8 piece &nbsp;&nbsp;(2 flv'rs)<br>10 piece &nbsp;(2 flv'rs)</div>
  <div class="abs cond" style="left:214px;top:584px;font-size:12.5px;line-height:18px">$9.19<br>$11.19<br>$12.99</div>
  <div class="abs cond" style="left:267px;top:584px;font-size:12.5px;line-height:18px">$10.29<br>$12.09<br>$13.99</div>
  <div class="abs cond" style="left:324px;top:584px;font-size:12.5px;line-height:18px">$10.29<br>$12.29<br>$14.19</div>
  <div class="abs wide red" style="left:86px;top:668px;font-size:15px;letter-spacing:.5px">Tenders</div>
  <div class="abs wide" style="left:86px;top:692px;font-size:13px;line-height:18px;letter-spacing:.9px">3 piece (1 flvr&amp; 1 dip)<br>5 piece (1 flvr&amp; 1 dip)<br>8 piece &nbsp;(2 flv'rs 2 dips)</div>
  <div class="abs wide" style="left:286px;top:692px;font-size:13px;line-height:18px;letter-spacing:.9px;text-align:right;width:76px">$8.79<br>$10.69<br>$19.49</div>
  <div class="band" style="left:66px;top:766px;width:327px;height:18px;font-size:8px;line-height:18px">All Combos come with Fries, Dips, Veggies, and 20oz Fountain Drink</div>

  <!-- Drinks -->
  <div class="frame" style="left:447px;top:490px;width:386px;height:221px"></div>
  <div class="ribbon" style="left:574px;top:474px;width:132px;height:36px">
    <svg viewBox="0 0 100 30" preserveAspectRatio="none"><polygon points="0,0 100,0 94,15 100,30 0,30 6,15" fill="#d9261c"/><polygon points="4,3 96,3 91,15 96,27 4,27 9,15" fill="none" stroke="#fff" stroke-dasharray="1 2" vector-effect="non-scaling-stroke"/></svg>
    <span style="font-size:20px">DRINKS</span>
  </div>
  <div class="abs cond" style="left:464px;top:520px;font-size:11.5px">Fizz Co.</div>
  <div class="abs cond" style="left:628px;top:520px;font-size:11.5px">Frozen Margaritas &amp; Daiquiris</div>
  <div class="abs cond" style="left:464px;top:556px;font-size:11.5px;line-height:19px">Cola. Diet Cola. &nbsp;Dr. Spice.<br>Lemon-Lime.Strawberry. Orange.</div>
  <div class="abs cond" style="left:637px;top:556px;font-size:11.5px">Strawberry. &nbsp;Blue Hawaiian. Hurricane</div>
  <div class="abs cond" style="left:464px;top:611px;font-size:11.5px">20 oz &nbsp;I &nbsp;32 oz &nbsp;Fountain</div>
  <div class="abs cond" style="left:464px;top:648px;font-size:11.5px">$2.29 &nbsp;&nbsp;$2.89</div>
  <div class="divider" style="left:587px"></div>
  <div class="divider" style="left:638px"></div>
  <div class="divider" style="left:705px"></div>
  <div class="divider" style="left:764px"></div>
  <div class="abs cond" style="left:599px;top:611px;font-size:11.5px">Single</div>
  <div class="abs cond" style="left:644px;top:611px;font-size:11.5px">The Big Ole'</div>
  <div class="abs cond" style="left:714px;top:611px;font-size:11.5px">Half Gal.</div>
  <div class="abs cond" style="left:782px;top:611px;font-size:11.5px">1 Gal.</div>
  <div class="abs cond" style="left:601px;top:648px;font-size:11.5px;line-height:18px;text-align:center">16oz.<br>$6.89</div>
  <div class="abs cond" style="left:661px;top:648px;font-size:11.5px;line-height:18px;text-align:center">32 oz.<br>$12.89</div>
  <div class="abs cond" style="left:714px;top:648px;font-size:11.5px;line-height:18px;text-align:center">64 oz.<br>$22.89</div>
  <div class="abs cond" style="left:779px;top:648px;font-size:11.5px;line-height:18px;text-align:center">128 oz<br>$41.99</div>

  <!-- Xtra dips -->
  <div class="ribbon" style="left:447px;top:725px;width:117px;height:24px">
    <svg viewBox="0 0 100 30" preserveAspectRatio="none"><polygon points="0,0 100,0 94,15 100,30 0,30 6,15" fill="#d9261c"/><polygon points="4,3 96,3 91,15 96,27 4,27 9,15" fill="none" stroke="#fff" stroke-dasharray="1 2" vector-effect="non-scaling-stroke"/></svg>
    <span style="font-size:13px;font-weight:400">XTRA DIPS</span>
  </div>
  <div class="abs wide" style="left:444px;top:754px;font-size:10.5px;line-height:16px;font-weight:700;letter-spacing:.2px">Ranch &nbsp;I Cheese sauce I Honey Mustard<br>I Bleu Cheese &nbsp;I &nbsp;Spicy Ranch I</div>
  <div class="price-box" style="left:444px;top:788px;width:67px;height:21px">$0.79</div>

  <!-- Xtra flavors -->
  <div class="ribbon" style="left:856px;top:482px;width:145px;height:27px">
    <svg viewBox="0 0 100 30" preserveAspectRatio="none"><polygon points="0,0 100,0 94,15 100,30 0,30 6,15" fill="#d9261c"/><polygon points="4,3 96,3 91,15 96,27 4,27 9,15" fill="none" stroke="#fff" stroke-dasharray="1 2" vector-effect="non-scaling-stroke"/></svg>
    <span style="font-size:15px;font-weight:400">XTRA &nbsp;FLAVORS</span>
  </div>
  <div class="abs wide" style="left:857px;top:516px;font-size:11px;line-height:16.3px;font-weight:700;letter-spacing:.35px">The Reaper I Traditional Hot<br>I New Orleans Spicy I &nbsp;Spicy Korean BBQ<br>I Spicy Garlic I Bangin Jamaican Jerk<br>I Mango Haberero I Pineapple BangIGojugang<br>I &nbsp;Mild I Texas BBQ I Teriyaki I &nbsp;Garlic Parmesan<br>I Lemon Pepper I Honey BBQ</div>
  <div class="price-box" style="left:862px;top:623px;width:68px;height:20px">$1.09</div>

  <!-- Dessert -->
  <div class="ribbon" style="left:856px;top:680px;width:127px;height:27px">
    <svg viewBox="0 0 100 30" preserveAspectRatio="none"><polygon points="0,0 100,0 94,15 100,30 0,30 6,15" fill="#d9261c"/><polygon points="4,3 96,3 91,15 96,27 4,27 9,15" fill="none" stroke="#fff" stroke-dasharray="1 2" vector-effect="non-scaling-stroke"/></svg>
    <span style="font-size:18px">DESSERT</span>
  </div>
  <div class="abs wide" style="left:862px;top:714px;font-size:12.5px;line-height:14.3px;letter-spacing:.5px">Cheesecake Plain<br>I Strawberry Swirl<br>I &nbsp;Raspberry<br>I Chocolate Chip</div>
  <div class="price-box" style="left:862px;top:787px;width:68px;height:20px">$4.99</div>
</div>
</body>
</html>
```